Software Application page - product section

I have developed a proposal generation application and want to improve the main user interface page.
This is the most important and most used page within my application and therefore it needs to look slick, clean, simple and easy to understand whilst looking very professional, creditable and established.
This is the page in which the user makes certain selections of products and the system will in turn display information on the product selected. The user can then add the product to the basket and the system also calculates the monthly cost of the product along with the profit the user makes by offering the particular product.
I have put something together myself and uploaded accordingly to give you an idea as to what it currently looks like and the structure that it needs to follow.
Section 1
This displays the Customer's account, proposal ID, Customer name etc
Section 2
I have these as radio buttons that the user selects, then clicks on the 'Search product' button. The items will then be displayed in section 3
Section 3
This datagrid displays the available products based on the section 2's selections
Section 4
shows information on the product that has been highlighed in section 3's datagrid. The user then clicks in qty field to enter the qty and then clicks the ADD shopping basket button to add the product to the basket in section 5 datagrid.
Section 5
This is the datagrid/shopping basket that displays all the products that the user has added.
Section 6
Displays all the figures including the total qtys', costs, revenue etc
WHILST IT IS IMPORTANT THAT THE DESIGN MUST FOLLOW THE STRUCTURE OF WHAT IS ATTACHED. I MUST POINT OUT THAT I AM NOT HAPPY WITH THE CURRENT DESIGN. I DO NOT LIKE THE LOOK AND FEEL OF THE CURRENT DESIGN AS IT LOOKS CHEAP AND AMATEURISH.
THE RADIO BUTTONS IN SECTION 1 FOR EXAMPLE SHOULD BE MORE CREATIVE, THE SIZE OF EACH SECTIONS CURRENTLY LOOK DISPROPORTIONATE. THE COLOURS ARE ALL OVER THE PLACE.
THE SIZE OF PAGE MUST BE 1009 X 689
PLEASE VISIT OUT OUR WEBSITE TO STICK TO THE COMPANIES BRAND: www.velantix.co.uk
I have other pages within my application that require designs along with icons and a lot of work on the website also require redesigning so the best design will also be given this work
Many thanks
Marcus

```html
<!DOCTYPE html>
<html lang="en">
<head>
<meta charset="utf-8">
<title>Velantix – Proposal Product Selection</title>
<link rel="stylesheet" href="https://fonts.googleapis.com/css2?family=Fira+Sans:wght@400;500;600&display=swap">
<style>
:root{
  --page:#f8eafa;
  --brand:#7b3d9a;
  --brand-dark:#5c2870;
  --brand-text:#6d3a88;
  --accent-text:#c56fc8;
  --btn-top:#bd66cf;
  --btn-bottom:#8c3fa3;
  --sel-top:#f6911c;
  --sel-bottom:#d8550a;
  --head-top:#7d4291;
  --head-bottom:#4a1d5c;
  --row-alt:#e2c3e7;
  --row:#ffffff;
  --cell-text:#5b3a66;
  --panel:#dcbde4;
  --panel-band:#c49bcf;
  --field:#f7e6f9;
  --field-text:#c36fc9;
  --scroll:#8a4aa0;
  --total-light:#f1dff4;
  --total-dark:#e2c3e7;
}
*{box-sizing:border-box;margin:0;padding:0}
html,body{width:1200px;height:819px;overflow:hidden;background:var(--page)}
body{font-family:"Fira Sans",sans-serif;color:var(--cell-text)}
.canvas{width:1200px;height:819px;overflow:hidden;position:relative}
.stage{position:absolute;left:0;top:0;width:1009px;height:689px;transform:scale(1.1893);transform-origin:0 0}
.abs{position:absolute}

/* customer card */
.customer-card{left:25px;top:26px;width:463px;height:77px;background:#fff;box-shadow:0 1px 2px rgba(90,40,110,.2)}
.avatar{left:0;top:0;width:95px;height:77px;background:var(--brand);display:flex;align-items:center;justify-content:center}
.customer-name{left:112px;top:12px;font-size:18px;font-weight:500;color:var(--brand-text)}
.customer-meta{left:112px;top:37px;font-size:12px;line-height:13px;color:var(--brand-text);font-weight:600}
.customer-meta span{color:var(--accent-text);font-weight:400}
.status{left:361px;top:0;width:102px;height:77px;border-left:1px solid #e4d2e8;text-align:center;font-size:12px;font-weight:600;color:#5a3a68;padding-top:11px}
.status svg{display:block;margin:6px auto 0}

/* option buttons */
.option{position:absolute;height:37px;display:flex;align-items:center;justify-content:center;color:#fff;font-size:16px;font-weight:500;
  background:linear-gradient(var(--btn-top),var(--btn-bottom));border-right:1px solid #6a2c80;box-shadow:inset 0 1px 0 rgba(255,255,255,.3)}
.option.is-selected{background:linear-gradient(var(--sel-top),var(--sel-bottom))}
.option.first{border-radius:6px 0 0 6px}
.option.last{border-radius:0 6px 6px 0;border-right:0}

.search-bar{left:25px;top:310px;width:463px;height:47px;background:var(--brand);color:#fff;font-size:15px;letter-spacing:2.5px;font-weight:500;padding:15px 0 0 37px}
.search-btn{right:0;top:0;width:73px;height:47px;background:var(--brand-dark);display:flex;align-items:center;justify-content:center}

/* grids */
.grid{background:#fff;overflow:hidden}
.grid-head{position:absolute;left:0;right:0;top:0;height:30px;background:linear-gradient(var(--head-top),var(--head-bottom));color:#fff;font-size:13px;font-weight:500}
.cell{position:absolute;font-size:13px;white-space:nowrap}
.row{position:absolute;left:0;right:0}
.row:nth-child(even){background:var(--row-alt)}
.vline{position:absolute;top:0;bottom:0;width:1px;background:#8a6a94}
.vscroll{position:absolute;width:14px;background:#f2e4f4;border-left:1px solid #d6bedc}
.vscroll i{position:absolute;left:3px;width:7px;border-radius:4px;background:var(--scroll)}
.hscroll{position:absolute;left:0;right:0;height:15px;background:#f2e4f4;border-top:1px solid #d6bedc}
.hscroll i{position:absolute;top:4px;height:7px;border-radius:4px;background:var(--scroll)}

/* product details */
.details{left:519px;top:26px;width:465px;height:154px;background:var(--panel)}
.details-title{left:27px;top:12px;font-size:13px;color:#6b4a7a;letter-spacing:.3px}
.field{position:absolute;height:24px;background:var(--field);border-radius:3px;font-size:12.5px;color:var(--field-text);padding:5px 0 0 11px}
.details-band{left:0;right:0;bottom:0;height:28px;background:var(--panel-band)}
.action{position:absolute;height:24px;background:var(--brand-dark);color:#fff;border-radius:3px;font-size:12.5px;font-weight:500;letter-spacing:1.5px;display:flex;align-items:center;justify-content:center;gap:9px}
.action b{display:inline-block;width:14px;height:14px;border:1px solid #fff;font-size:10px;line-height:12px;text-align:center;font-weight:500;letter-spacing:0}

.delete-band{left:519px;top:373px;width:465px;height:28px;background:var(--panel-band)}

.total{position:absolute;top:0;height:47px;font-size:13px;display:flex;align-items:center}
.pager{position:absolute;top:641px;width:23px;height:22px;background:#fff;border:1px solid #d3bcd8;display:flex;align-items:center;justify-content:center}
</style>
</head>
<body>
<div class="canvas">
<div class="stage">

  <!-- customer -->
  <section class="abs customer-card">
    <div class="abs avatar">
      <svg width="40" height="44" viewBox="0 0 40 44" aria-hidden="true"><path fill="#fff" d="M20 3c-6 0-9 4-9 10 0 4 2 8 4 10v3c-7 2-13 5-13 11v4h36v-4c0-6-6-9-13-11v-3c2-2 4-6 4-10 0-6-3-10-9-10z"/></svg>
    </div>
    <div class="abs customer-name">Velantix Test Ltd</div>
    <div class="abs customer-meta">Proposal ID: <span>1334235</span><br>Customer ID: <span>110399</span></div>
    <div class="abs status">Status:
      <svg width="24" height="28" viewBox="0 0 24 28" aria-hidden="true">
        <rect x="2" y="4" width="16" height="20" rx="1.5" fill="#7b3d9a"/>
        <rect x="6" y="2" width="8" height="5" rx="1" fill="#5c2870"/>
        <circle cx="17" cy="21" r="5.5" fill="#ef8a5a" stroke="#fff" stroke-width="1.5"/>
        <rect x="14" y="20.2" width="6" height="1.6" fill="#fff"/>
      </svg>
    </div>
  </section>

  <!-- selection options -->
  <div class="option first" style="left:25px;top:109px;width:158px">Mobile</div>
  <div class="option is-selected" style="left:183px;top:109px;width:148px">Fixed Line</div>
  <div class="option last" style="left:331px;top:109px;width:157px">Other Products</div>

  <div class="option first" style="left:25px;top:148px;width:108px">N4</div>
  <div class="option is-selected" style="left:133px;top:148px;width:118px">Solenta</div>
  <div class="option is-selected" style="left:251px;top:148px;width:98px">QX</div>
  <div class="option last" style="left:349px;top:148px;width:139px">Amber</div>

  <div class="option first" style="left:25px;top:187px;width:226px">New</div>
  <div class="option is-selected last" style="left:251px;top:187px;width:237px">Resign</div>

  <div class="option first" style="left:25px;top:226px;width:88px">12</div>
  <div class="option is-selected" style="left:113px;top:226px;width:61px">24</div>
  <div class="option" style="left:174px;top:226px;width:61px">36</div>
  <div class="option" style="left:235px;top:226px;width:61px">48</div>
  <div class="option" style="left:296px;top:226px;width:61px">60</div>
  <div class="option last" style="left:357px;top:226px;width:131px">Other</div>

  <div class="option first" style="left:25px;top:265px;width:163px">Share Plan</div>
  <div class="option is-selected" style="left:188px;top:265px;width:118px">Single Plan</div>
  <div class="option" style="left:306px;top:265px;width:55px">MBB</div>
  <div class="option last" style="left:361px;top:265px;width:127px">Add-on</div>

  <div class="abs search-bar">SEARCH PRODUCT
    <div class="abs search-btn">
      <svg width="30" height="30" viewBox="0 0 30 30" aria-hidden="true"><circle cx="17" cy="12" r="8" fill="none" stroke="#fff" stroke-width="3"/><path d="M11 18 4 25" stroke="#fff" stroke-width="4" stroke-linecap="round"/></svg>
    </div>
  </div>

  <!-- tariff grid -->
  <section class="abs grid" style="left:25px;top:370px;width:463px;height:290px">
    <div class="grid-head"><span class="cell" style="left:18px;top:8px">Tariff</span><span class="cell" style="left:336px;top:8px">Price</span></div>
    <div class="abs" style="left:0;right:0;top:30px;height:245px">
      <div class="row" style="top:0;height:35px"><span class="cell" style="left:18px;top:12px">Business Single 300</span><span class="cell" style="left:336px;top:12px">19.03</span></div>
      <div class="row" style="top:35px;height:35px"><span class="cell" style="left:18px;top:10px">Business Single 600</span><span class="cell" style="left:336px;top:10px">25.09</span></div>
      <div class="row" style="top:70px;height:35px"><span class="cell" style="left:18px;top:9px">Best For Business PAYU</span><span class="cell" style="left:336px;top:9px">12.56</span></div>
      <div class="row" style="top:105px;height:35px"><span class="cell" style="left:18px;top:10px">Best For Business PAYU Unlimited</span><span class="cell" style="left:336px;top:10px">22.75</span></div>
      <div class="row" style="top:140px;height:35px"><span class="cell" style="left:18px;top:9px">Business Single 50</span><span class="cell" style="left:336px;top:9px">12.11</span></div>
      <div class="row" style="top:175px;height:35px"><span class="cell" style="left:18px;top:9px">Business Single On &amp; Oil</span><span class="cell" style="left:336px;top:9px">32.14</span></div>
      <div class="row" style="top:210px;height:35px"><span class="cell" style="left:18px;top:8px">Business Single On &amp; Oil &amp; In</span><span class="cell" style="left:336px;top:8px">53.55</span></div>
    </div>
    <div class="vline" style="left:318px"></div>
    <div class="vscroll" style="left:449px;top:0;bottom:15px"><i style="top:38px;height:66px"></i></div>
    <div class="hscroll" style="bottom:0"><i style="left:32px;width:68px"></i></div>
  </section>

  <!-- product details -->
  <section class="abs details">
    <div class="abs details-title">PRODUCT DETAILS</div>
    <div class="field" style="left:27px;top:35px;width:162px">Product</div>
    <div class="field" style="left:197px;top:35px;width:112px">Qty</div>
    <div class="field" style="left:317px;top:35px;width:112px">Tariff Cost</div>
    <div class="field" style="left:27px;top:64px;width:162px">Revenue %</div>
    <div class="field" style="left:197px;top:64px;width:112px">Minutes</div>
    <div class="field" style="left:317px;top:64px;width:112px">Texts</div>
    <div class="field" style="left:27px;top:94px;width:402px">Data</div>
    <div class="abs details-band">
      <div class="action" style="left:27px;top:2px;width:192px"><b>?</b>INFORMATION</div>
      <div class="action" style="left:237px;top:2px;width:192px"><b>+</b>SUBMIT INFO</div>
    </div>
  </section>

  <!-- product grid -->
  <section class="abs grid" style="left:519px;top:190px;width:465px;height:183px">
    <div class="grid-head"><span class="cell" style="left:18px;top:9px">Product</span><span class="cell" style="left:256px;top:9px">Type</span><span class="cell" style="left:337px;top:9px">Price</span><span class="cell" style="left:406px;top:9px">QTY</span></div>
    <div class="abs" style="left:0;right:0;top:31px;height:137px">
      <div class="row" style="top:0;height:27px"><span class="cell" style="left:18px;top:6px">Business Single 300</span><span class="cell" style="left:256px;top:6px">Lorem</span><span class="cell" style="left:337px;top:6px">19.03</span></div>
      <div class="row" style="top:27px;height:27px"><span class="cell" style="left:18px;top:6px">Business Single 600</span><span class="cell" style="left:256px;top:6px">Lorem</span><span class="cell" style="left:337px;top:6px">25.09</span></div>
      <div class="row" style="top:54px;height:27px"><span class="cell" style="left:18px;top:6px">Best For Business PAYU</span><span class="cell" style="left:256px;top:6px">Lorem</span><span class="cell" style="left:337px;top:6px">12.56</span></div>
      <div class="row" style="top:81px;height:27px"><span class="cell" style="left:18px;top:6px">Best For Business PAYU Unlimited</span><span class="cell" style="left:256px;top:6px">Lorem</span><span class="cell" style="left:337px;top:6px">22.75</span></div>
      <div class="row" style="top:108px;height:29px"><span class="cell" style="left:18px;top:6px">Business Single 50</span><span class="cell" style="left:256px;top:6px">Lorem</span><span class="cell" style="left:337px;top:6px">12.11</span></div>
    </div>
    <div class="vline" style="left:238px"></div>
    <div class="vline" style="left:311px"></div>
    <div class="vline" style="left:392px"></div>
    <div class="vscroll" style="left:449px;top:0;bottom:15px"><i style="top:38px;height:66px"></i></div>
    <div class="hscroll" style="bottom:0"><i style="left:32px;width:68px"></i></div>
  </section>
  <div class="abs delete-band">
    <div class="action" style="left:137px;top:2px;width:192px"><b>−</b>DELETE ITEM</div>
  </div>

  <!-- basket grid -->
  <section class="abs grid" style="left:519px;top:417px;width:465px;height:215px">
    <div class="grid-head"><span class="cell" style="left:18px;top:9px">Product</span><span class="cell" style="left:201px;top:9px">Qty</span><span class="cell" style="left:251px;top:9px">Monthly Cost</span><span class="cell" style="left:345px;top:9px">Monthly Revenue</span></div>
    <div class="abs" style="left:0;right:0;top:32px;height:136px">
      <div class="row" style="top:0;height:27px"><span class="cell" style="left:18px;top:6px">Mobile Voice</span><span class="cell" style="left:207px;top:6px">0</span><span class="cell" style="left:286px;top:6px">0</span><span class="cell" style="left:376px;top:6px">19.03</span></div>
      <div class="row" style="top:27px;height:27px"><span class="cell" style="left:18px;top:6px">Mobile Data Only</span><span class="cell" style="left:207px;top:6px">0</span><span class="cell" style="left:286px;top:6px">0</span><span class="cell" style="left:376px;top:6px">25.09</span></div>
      <div class="row" style="top:54px;height:27px"><span class="cell" style="left:18px;top:6px">Mobile Total</span><span class="cell" style="left:207px;top:6px">0</span><span class="cell" style="left:286px;top:6px">0</span><span class="cell" style="left:376px;top:6px">12.56</span></div>
      <div class="row" style="top:81px;height:27px"><span class="cell" style="left:18px;top:6px">Fixed Line</span><span class="cell" style="left:208px;top:6px">-</span><span class="cell" style="left:286px;top:6px">0</span><span class="cell" style="left:376px;top:6px">22.75</span></div>
      <div class="row" style="top:108px;height:28px"><span class="cell" style="left:18px;top:6px">Other Products</span><span class="cell" style="left:208px;top:6px">-</span><span class="cell" style="left:286px;top:6px">0</span><span class="cell" style="left:376px;top:6px">12.11</span></div>
    </div>
    <div class="vline" style="left:178px;bottom:47px"></div>
    <div class="vline" style="left:248px;bottom:47px"></div>
    <div class="vline" style="left:337px;bottom:47px"></div>
    <div class="abs" style="left:0;right:0;top:168px;height:47px">
      <div class="total" style="left:0;width:150px;background:var(--total-light);padding-left:18px">Total Monthly Cost</div>
      <div class="total" style="left:150px;width:83px;background:var(--total-dark);justify-content:center">0</div>
      <div class="total" style="left:233px;width:147px;background:var(--total-light);padding-left:6px">Total Monthly Revenue</div>
      <div class="total" style="left:380px;width:85px;background:var(--total-dark);justify-content:center">999999.00</div>
    </div>
  </section>

  <div class="pager" style="left:930px"><svg width="8" height="12" viewBox="0 0 8 12" aria-hidden="true"><path d="M6 1 1 6l5 5" fill="none" stroke="#333" stroke-width="1.8"/></svg></div>
  <div class="pager" style="left:959px"><svg width="8" height="12" viewBox="0 0 8 12" aria-hidden="true"><path d="m2 1 5 5-5 5" fill="none" stroke="#333" stroke-width="1.8"/></svg></div>

</div>
</div>
</body>
</html>
```